(Harbour Roastworks) sourcing coffee related material and services

we are a start up that provide all coffee related items for coffee shops and coffee fanatics. However, we mostly offer coffee machines customization that includes paint replacement and wood modification. we also focus on providing training for barista and coffee lovers.

we are looking for the following:

1-Design a logo that will be used for social media application and official paper work requirements

2- Design a business card (square shaped 2"*2") adopting the same logo and identity. please allow for adding mobile number, snapchat, and instgram accounts in the card.

3- Design a very basic monogram stamp by adding the three character (R4T) the number (2) shall be small in size just like how the numbers written in chemical formal.

Please take a quick look to instagram page to have a idea about the our start up

https://www.pixgram.example/harbour_roastworks/

Target Market(s)

coffeeshop owners and coffee fanatics

Industry/Entity Type

Coffee Shop

Contact Information for Business Card

R4T
Harbour Roastworks
editable text to add links to socail media

Logo Text

R4T

Font styles to use
Other font styles liked:
• flat design fonts

Colors

Designer to choose colors to be used in the design.

Requirements
Must have
• espresso portafilter, simple and minimal industrial look, wood,
Nice to have
• wood-making, portafilter, coffee beans, coffee tree,

```html
<!DOCTYPE html>
<html lang="en">
<head>
<meta charset="utf-8">
<title>Harbour Roastworks – Business Card</title>
<link rel="stylesheet" href="https://fonts.googleapis.com/css2?family=Josefin+Sans:wght@400;600&display=swap">
<style>
  :root {
    --page-bg: #ffffff;
    --bean-dark: #3a2112;
    --bean-mid: #6b4126;
    --bean-light: #8f5d3a;
    --burlap: #dcc49c;
    --burlap-light: #e8d6b4;
    --brand-red: #5a0c0c;
    --card-back: #3b0000;
    --frame-line: #d9b8a0;
    --back-text: #f4e6da;
  }
  * { box-sizing: border-box; margin: 0; padding: 0; }
  html, body {
    width: 1200px;
    height: 670px;
    overflow: hidden;
    background: var(--page-bg);
  }
  .canvas {
    position: relative;
    width: 1200px;
    height: 670px;
    font-family: "Josefin Sans", sans-serif;
  }
  .card {
    position: absolute;
    top: 82px;
    width: 506px;
    height: 506px;
    overflow: hidden;
  }
  .card--front { left: 72px; }
  .card--back { left: 622px; background: var(--card-back); }

  .bean-backdrop {
    position: absolute;
    inset: 0;
    background: radial-gradient(circle at 50% 50%, var(--bean-light) 0%, var(--bean-mid) 45%, var(--bean-dark) 100%);
  }
  .burlap-patch {
    position: absolute;
    left: 55px;
    top: 55px;
    width: 400px;
    height: 400px;
    background: radial-gradient(circle at 50% 50%, var(--burlap-light) 0%, var(--burlap) 100%);
  }
  .brand-ring {
    position: absolute;
    left: 105px;
    top: 105px;
    width: 296px;
    height: 296px;
    border: 3px solid var(--brand-red);
    border-radius: 50%;
  }
  .brand-name {
    position: absolute;
    left: 0;
    right: 0;
    top: 200px;
    text-align: center;
    color: var(--brand-red);
    font-weight: 400;
    font-size: 36px;
    line-height: 48px;
    letter-spacing: 1px;
  }
  .brand-monogram {
    position: absolute;
    left: 0;
    right: 0;
    top: 310px;
    text-align: center;
    color: var(--brand-red);
    font-weight: 400;
    font-size: 24px;
  }

  .back-frame {
    position: absolute;
    inset: 37px;
    border: 1px solid var(--frame-line);
  }
  .contact {
    position: absolute;
    left: 0;
    right: 0;
    text-align: center;
    color: var(--back-text);
    font-weight: 400;
    white-space: nowrap;
  }
  .contact--name { top: 110px; font-size: 27px; font-weight: 600; }
  .contact--name .surname { font-variant: small-caps; letter-spacing: 1px; }
  .contact--title { top: 165px; font-size: 20px; letter-spacing: 1.5px; }
  .contact--phone { top: 245px; font-size: 27px; letter-spacing: 1.5px; }
  .contact--email { top: 292px; font-size: 23px; letter-spacing: 0.5px; }
  .contact--web { top: 374px; font-size: 23px; letter-spacing: 0.5px; }
</style>
</head>
<body>
<main class="canvas">
  <section class="card card--front">
    <div class="bean-backdrop" role="img" aria-label="Photograph of roasted coffee beans filling the card"></div>
    <div class="burlap-patch" role="img" aria-label="Square of frayed burlap fabric"></div>
    <div class="brand-ring"></div>
    <p class="brand-name">Harbour<br>Roastworks</p>
    <p class="brand-monogram">R4T</p>
  </section>

  <section class="card card--back">
    <div class="back-frame"></div>
    <p class="contact contact--name">Firstname <span class="surname">Lastname</span></p>
    <p class="contact contact--title">BUSINESS TITLE</p>
    <p class="contact contact--phone">1234 5678 9000</p>
    <p class="contact contact--email">name@website.com</p>
    <p class="contact contact--web">www.website.com</p>
  </section>
</main>
</body>
</html>
```